Product label design for detailing products

We want an outstanding but still chique label design for our car/motorcycle detailing products. We are mainly in the motor racing industry and also want to show our racing mentality.
Attached is our current design, which is pretty simple, and our logo. We want an unique design with our main colors yellow (ffcc00) and black.
We use font Anton.
For inspiration you can view some of our competitors: Varex, Zin-Gap.

To see our items you can visit our webshop: www.the-gridlane.eu

Target Market(s)

Customers that are willing to polish there cars / motorcycle in a professional way

Industry/Entity Type

detailing, poloshing, racing and maintenance

Other font styles liked:
• Anton

Designer to choose colors to be used in the design.

Requirements
Must have
• Luxurious look, racey vibes, unique and outstanding - Not only for motorcycles also for cars so a more universal look
Nice to have
• Some hexagon lights built in, a fresh new design which is not seen before, creative and really shows what our company is able for
Should not have
• easy, simple designs

```html
<!DOCTYPE html>
<html lang="en">
<head>
<meta charset="utf-8">
<title>Fire Suds Label</title>
<link rel="stylesheet" href="https://fonts.googleapis.com/css2?family=Anton&family=Barlow+Condensed:wght@800&display=swap">
<style>
  :root {
    --page: #dcdcdc;
    --ink: #141414;
    --panel-edge: #0b0b0c;
    --panel-mid: #26282b;
    --yellow: #ffcc00;
    --yellow-deep: #e0a400;
    --white: #f3f3f3;
    --hex-glow: #4a3d12;
  }
  * { box-sizing: border-box; margin: 0; padding: 0; }
  html, body { width: 1034px; height: 1200px; overflow: hidden; }
  body {
    background: linear-gradient(180deg, #c8c8c8 0%, var(--page) 55%, #ececec 100%);
    position: relative;
  }
  .label { position: absolute; left: 270px; top: 27px; width: 493px; height: 1145px; }
  .label-panel {
    position: absolute; inset: 0 0 65px 0;
    background: linear-gradient(90deg, var(--panel-edge) 0%, var(--panel-mid) 50%, var(--panel-edge) 100%);
  }
  .label-art { position: absolute; inset: 0; }
  .hex-field {
    position: absolute;
    background: radial-gradient(ellipse at center, var(--hex-glow) 0%, rgba(40,34,14,0.35) 55%, transparent 80%);
    opacity: 0.55;
  }
  .hex-field--top-left { left: 20px; top: 40px; width: 150px; height: 160px; }
  .hex-field--top-right { left: 400px; top: 0; width: 93px; height: 140px; }
  .hex-field--bottom { left: 90px; top: 800px; width: 280px; height: 270px; }

  .brand {
    position: absolute; left: 0; right: 0; top: 200px;
    display: flex; justify-content: center; align-items: center; gap: 14px;
  }
  .brand-mark { width: 16px; height: 16px; background: var(--yellow); }
  .brand-name {
    font-family: "Anton", sans-serif; font-size: 44px; line-height: 1;
    color: var(--white); letter-spacing: 3px;
  }

  .product-name {
    position: absolute; left: 0; right: 0; text-align: center;
    font-family: "Barlow Condensed", sans-serif; font-weight: 800;
    color: var(--white); line-height: 1; font-size: 184px;
  }
  .product-name--first { top: 350px; }
  .product-name--second { top: 530px; }

  .claim {
    position: absolute; left: 70px; top: 742px; width: 360px; height: 42px;
    background: var(--yellow); transform: rotate(-0.8deg);
    display: flex; align-items: center; justify-content: center;
    font-family: "Anton", sans-serif; font-size: 19px; color: var(--ink);
  }

  .footer-band { position: absolute; left: 0; right: 0; top: 1080px; height: 65px; background: var(--white); }
  .footer-line { position: absolute; left: 0; right: 0; height: 3px; background: var(--yellow-deep); }
  .footer-line--upper { top: 24px; }
  .footer-line--lower { top: 32px; background: var(--ink); height: 2px; }
  .footer-tab {
    position: absolute; left: 80px; width: 332px; top: 6px; height: 54px;
    background: var(--ink); display: flex; align-items: center; justify-content: center;
    font-family: "Anton", sans-serif; font-size: 20px; letter-spacing: 3px; color: var(--white);
  }
</style>
</head>
<body>
  <main class="label">
    <div class="label-panel"></div>

    <div class="hex-field hex-field--top-left" role="img" aria-label="Faint golden hexagon light pattern"></div>
    <div class="hex-field hex-field--top-right" role="img" aria-label="Faint golden hexagon light pattern"></div>
    <div class="hex-field hex-field--bottom" role="img" aria-label="Faint golden hexagon light pattern"></div>

    <svg class="label-art" viewBox="0 0 493 1145" width="493" height="1145" aria-hidden="true">
      <defs>
        <linearGradient id="edge-band" x1="0" x2="1" y1="0" y2="0">
          <stop offset="0" stop-color="#d99d00"/>
          <stop offset="1" stop-color="#ffcc00"/>
        </linearGradient>
      </defs>
      <g fill="url(#edge-band)">
        <rect x="0" y="300" width="10" height="720"/>
        <polygon points="18,330 40,300 40,420 18,450"/>
        <polygon points="18,520 40,490 40,610 18,640"/>
        <polygon points="18,710 40,680 40,800 18,830"/>
        <polygon points="18,900 40,870 40,990 18,1020"/>
        <rect x="483" y="180" width="10" height="820"/>
        <polygon points="453,240 475,210 475,330 453,360"/>
        <polygon points="453,430 475,400 475,520 453,550"/>
        <polygon points="453,620 475,590 475,710 453,740"/>
        <polygon points="453,810 475,780 475,900 453,930"/>
      </g>
    </svg>

    <div class="brand">
      <span class="brand-mark"></span>
      <span class="brand-name">GRIDLANE</span>
    </div>

    <h1 class="product-name product-name--first">FIRE</h1>
    <p class="product-name product-name--second">SUDS</p>

    <p class="claim">ULTRA-DENSE CLINGING FIRE SUDS</p>

    <footer class="footer-band">
      <span class="footer-line footer-line--upper"></span>
      <span class="footer-line footer-line--lower"></span>
      <span class="footer-tab">CLEANED FOR THE PODIUM</span>
    </footer>
  </main>
</body>
</html>
```